Wordpress Design Project

Good day.

I was hoping to buy a professional looking Wordpress template and just fill in the blanks with my personal data and start blogging, but unfortunately my blog posts need to include images that are 756 pixels x 439.

A sample image can be found at.
http://files.brelvanto.net/7-Pics/layoutsample.gif

So, I need your help.

1 This is a daily newsletter / blog site only. Not a corporate site.
2 Subject - Stock Market
2 I have no color preferences. I will leave that up to you.
I would like something that looks like this
http://preview.quillmark.net/aspect/
3 I would like to include Torvex Promos on both the Home Page and within each post.
4 The home page should show a link and a short summary to each post.
5 The home page should include an email capture box. We use MailChimp)
6 The home page should include a Site Search Box and function.
7 The home page should include a External Links Box.

If I have forgotten anything, please let me know.
I welcome your suggestions.

I look forward to seeing your designs and picking a winner.

Thank you for reading my post.

Marcus Pellingham

```html
<!DOCTYPE html>
<html lang="en">
<head>
<meta charset="utf-8">
<title>Marcus Pellingham – Commodity Blog</title>
<link href="https://fonts.googleapis.com/css2?family=Archivo+Black&family=Fjalla+One&family=Open+Sans:wght@400;600;700&display=swap" rel="stylesheet">
<style>
:root{
  --red:#e12a2a;
  --red-dark:#b81d1d;
  --ink:#2b2b2b;
  --text:#444;
  --muted:#777;
  --line:#d6d6d6;
  --panel:#e4e4e4;
  --page-bg:#ebebeb;
  --white:#fff;
  --footer:#2e2e2e;
  --footer-base:#1d1d1d;
  --link:#1a2fc9;
  --url:#1a8a2a;
  --ad-box:#d9d9d9;
}
*{box-sizing:border-box;margin:0;padding:0}
html,body{width:743px;height:1200px;overflow:hidden}
body{background:var(--page-bg);font-family:"Open Sans",Arial,sans-serif;color:var(--text)}
.page{position:relative;width:743px;height:1200px;overflow:hidden}
.sheet{position:absolute;left:71px;top:0;width:602px;height:1200px;background:var(--white);box-shadow:0 0 6px rgba(0,0,0,.18)}
.abs{position:absolute}

/* header */
.brand-name{left:17px;top:20px;font-family:"Archivo Black",sans-serif;font-size:23px;color:var(--ink);letter-spacing:.3px}
.brand-tag{left:19px;top:47px;font-size:13px;letter-spacing:6.6px;color:var(--ink)}
.connect{left:420px;top:20px;font-size:11px;color:var(--ink)}
.social{left:420px;top:40px;display:flex;gap:8px}
.social span{width:17px;height:17px;background:#5c5c5c;border-radius:2px}
.social span:first-child{border-radius:50%}

/* nav */
.nav{left:0;top:75px;width:602px;height:28px;border-top:1px solid var(--line);border-bottom:1px solid var(--line);background:#fafafa}
.nav a{position:absolute;top:4px;font-family:"Fjalla One",sans-serif;font-size:13px;color:var(--ink);text-decoration:none}
.nav .active{left:10px;top:2px;width:64px;height:24px;background:var(--red);color:var(--white);text-align:center;line-height:22px;border-radius:3px 3px 0 0}
.search{right:11px;top:7px;display:flex}
.search span{width:84px;height:14px;border:1px solid var(--line);font-size:7px;color:var(--muted);padding:2px 4px;background:var(--white)}
.search b{width:36px;height:14px;background:var(--red);color:var(--white);font-size:8px;font-weight:600;text-align:center;line-height:14px}

/* main */
.section-title{font-family:"Fjalla One",sans-serif;font-size:20px;color:var(--ink)}
.post{left:9px;width:433px}
.post-title{font-size:15px;color:var(--ink)}
.comments{position:absolute;right:22px;top:-2px;width:22px;height:19px;background:#262626;border-radius:50%;color:var(--white);font-size:9px;text-align:center;line-height:19px}
.comments::after{content:"";position:absolute;left:5px;bottom:-4px;border:4px solid transparent;border-top-color:#262626;border-left-color:#262626}
.meta{margin-top:6px;height:12px;background:#e8e8e8;font-size:6.5px;line-height:12px;padding-left:4px;color:#555}
.chart{display:block;margin-top:6px}
.excerpt{margin-top:20px;font-size:7.6px;line-height:10px;color:#333}
.more{display:block;margin-top:10px;font-size:6.5px;color:var(--red);text-decoration:underline}
.ad-slot{margin-top:8px;height:74px;background:var(--ad-box);border:1px solid #c8c8c8;font-family:"Archivo Black",sans-serif;font-size:33px;color:#b4b4b4;text-align:center;line-height:72px;letter-spacing:1px}
.divider{left:9px;width:433px;height:1px;background:var(--line)}

/* sidebar */
.side{left:458px;width:133px}
.side-title{font-family:"Fjalla One",sans-serif;font-size:15px;color:var(--ink)}
.news-box{top:136px;height:178px;background:#f6f6f6;border:1px solid #ececec;overflow:hidden}
.ribbon{position:absolute;left:-22px;top:14px;width:82px;height:15px;background:var(--red);color:var(--white);font-size:9px;text-align:center;line-height:15px;transform:rotate(-45deg)}
.wanna{position:absolute;right:8px;top:14px;text-align:right;font-size:10px;font-weight:700;color:var(--ink);line-height:12px}
.wanna b{display:block;font-family:"Fjalla One",sans-serif;font-weight:400;font-size:15px;color:var(--red);line-height:17px}
.news-note{position:absolute;left:8px;top:60px;font-size:6.5px;color:#333}
.field{position:absolute;left:10px;width:113px;height:13px;border:1px solid #bbb;background:var(--white);font-size:7px;color:var(--muted);padding:1px 5px}
.submit{position:absolute;left:28px;top:128px;width:80px;height:22px;background:linear-gradient(#4a4a4a,#111);border:2px solid #888;border-radius:5px;color:var(--white);font-family:"Fjalla One",sans-serif;font-size:13px;text-align:center;line-height:18px}
.privacy{position:absolute;left:0;right:0;top:158px;text-align:center;font-size:6.5px;color:#333}
.profile{top:329px;height:204px;background:var(--panel);padding:6px}
.photo{width:119px;height:75px;background:linear-gradient(#dcdcdc,#c7b7a8)}
.bio{margin-top:9px;font-size:6.8px;line-height:8.6px;color:#333}
.post-list{list-style:none}
.post-list li{position:relative;padding:5px 0 5px 15px;border-bottom:1px solid var(--line);font-size:7.3px;line-height:9px;color:#333}
.post-list li::before{content:"";position:absolute;left:2px;top:7px;width:7px;height:7px;background:var(--red)}
.archive{top:787px;height:37px;background:var(--panel);padding:11px 8px}
.select{position:relative;height:14px;background:var(--white);border:1px solid #bbb;font-size:7px;color:var(--muted);padding:1px 7px}
.select::after{content:"";position:absolute;right:0;top:0;width:12px;height:12px;background:#bbb}
.promos{top:840px;height:270px;border:1px solid var(--line);padding:6px 5px}
.promos h4{font-size:10px;font-weight:400;color:#222;margin-bottom:7px}
.promo{margin-bottom:7px;font-size:6.8px;line-height:8.4px;color:#222}
.promo a{display:block;font-size:8.6px;line-height:11px;color:var(--link);text-decoration:underline}
.promo i{font-style:normal;color:var(--url)}

/* footer */
.footer{left:0;top:1136px;width:602px;height:42px;background:var(--footer);text-align:center;font-size:8px;line-height:42px;color:#9a9a9a;word-spacing:2px}
.footer span{margin:0 17px}
.base{left:0;top:1178px;width:602px;height:22px;background:var(--footer-base);text-align:center;font-size:7px;line-height:22px;color:#777}
</style>
</head>
<body>
<div class="page">
<div class="sheet">

  <header>
    <div class="abs brand-name">Marcus Pellingham</div>
    <div class="abs brand-tag">Commodity Blog</div>
    <div class="abs connect">Connect with Me:</div>
    <div class="abs social" aria-label="Social links"><span></span><span></span><span></span><span></span><span></span><span></span><span></span></div>
  </header>

  <nav class="abs nav">
    <a class="active" href="#">Home</a>
    <a href="#" style="left:104px">About</a>
    <a href="#" style="left:163px">Blog</a>
    <a href="#" style="left:218px">Contacts</a>
    <div class="abs search"><span>Enter Keyword here</span><b>Search</b></div>
  </nav>

  <h2 class="abs section-title" style="left:9px;top:114px">Recent blog Post</h2>

  <svg width="0" height="0" style="position:absolute">
    <symbol id="price-chart" viewBox="0 0 433 242">
      <text x="0" y="10" font-family="Arial" font-size="7.5" font-weight="700" fill="#111">(WBP) Westbrook Petroleum-Daily&#160;&#160;&#160;&#160;06/18/2013</text>
      <text x="185" y="10" font-family="Arial" font-size="7.5" font-weight="700" fill="#e12a2a">C=92.43&#160;&#160;-.18&#160;&#160;-0.19%&#160;&#160;O=92.40</text>
      <text x="340" y="10" font-family="Arial" font-size="7.5" font-weight="700" fill="#111">H=93.25&#160;&#160;L=92.20</text>
      <g stroke="#eee" stroke-width="1">
        <line x1="0" y1="20" x2="400" y2="20"/><line x1="0" y1="44" x2="400" y2="44"/><line x1="0" y1="69" x2="400" y2="69"/><line x1="0" y1="93" x2="400" y2="93"/><line x1="0" y1="118" x2="400" y2="118"/><line x1="0" y1="142" x2="400" y2="142"/>
        <line x1="45" y1="15" x2="45" y2="160"/><line x1="100" y1="15" x2="100" y2="160"/><line x1="150" y1="15" x2="150" y2="160"/><line x1="205" y1="15" x2="205" y2="160"/><line x1="260" y1="15" x2="260" y2="160"/><line x1="315" y1="15" x2="315" y2="160"/><line x1="370" y1="15" x2="370" y2="160"/>
      </g>
      <line x1="400" y1="15" x2="400" y2="215" stroke="#e12a2a"/>
      <g font-family="Arial" font-size="7" fill="#111">
        <text x="404" y="22">96.00</text><text x="404" y="34">94.00</text><text x="404" y="46">92.00</text><text x="404" y="59">90.00</text><text x="404" y="71">88.00</text><text x="404" y="83">86.00</text><text x="404" y="95">84.00</text><text x="404" y="107">82.00</text><text x="404" y="120">80.00</text><text x="404" y="132">78.00</text><text x="404" y="144">76.00</text><text x="404" y="156">74.00</text>
        <text x="404" y="172">20.00</text><text x="404" y="193">0.00</text><text x="404" y="217">0.6000</text>
      </g>
      <polyline fill="none" stroke="#777" stroke-width="1" points="0,66 20,86 40,104 60,120 80,124 100,118 120,106 140,74 160,64 180,62 200,74 220,84 240,90 260,88 280,84 300,66 320,60 340,52 360,50 380,56 395,54"/>
      <polyline fill="none" stroke="#2a2ae8" stroke-width="1.6" points="0,81 10,87 20,106 30,112 40,124 50,136 60,139 70,130 80,136 90,124 100,133 110,112 120,93 130,69 140,57 150,51 160,57 170,69 180,75 190,57 200,63 210,87 220,106 230,112 240,99 250,81 260,90 270,106 280,93 290,69 300,63 310,57 320,39 330,32 340,14 350,26 360,20 370,32 380,29 395,30"/>
      <g fill="none" stroke="#e12a2a" stroke-width="1.6">
        <polyline points="0,81 10,87 20,106 30,112 40,124 50,136 60,139"/>
        <polyline points="200,63 210,87 220,106 230,112"/>
        <polyline points="260,90 270,106"/>
        <polyline points="340,14 350,26"/>
      </g>
      <g>
        <circle cx="18" cy="80" r="3.5" fill="#2a2ae8"/><circle cx="28" cy="104" r="3.5" fill="#e12a2a"/><circle cx="62" cy="128" r="3.5" fill="#2a2ae8"/><circle cx="84" cy="124" r="3.5" fill="#e12a2a"/><circle cx="98" cy="120" r="3.5" fill="#e12a2a"/><circle cx="108" cy="108" r="3.5" fill="#2a2ae8"/><circle cx="200" cy="94" r="3.5" fill="#e12a2a"/><circle cx="228" cy="104" r="3.5" fill="#e12a2a"/><circle cx="250" cy="92" r="3.5" fill="#2a2ae8"/><circle cx="282" cy="90" r="3.5" fill="#e12a2a"/><circle cx="347" cy="48" r="3.5" fill="#2a2ae8"/><circle cx="358" cy="40" r="3.5" fill="#e12a2a"/>
      </g>
      <line x1="0" y1="190" x2="400" y2="190" stroke="#999" stroke-width=".6"/>
      <path d="M0,190 C20,196 60,200 100,196 C115,194 120,192 128,190 Z" fill="#e12a2a"/>
      <path d="M128,190 C150,180 185,172 215,182 C220,186 224,189 228,190 Z" fill="#2a2ae8"/>
      <path d="M228,190 C245,195 275,195 292,190 Z" fill="#e12a2a"/>
      <path d="M292,190 C320,176 365,172 398,184 L398,190 Z" fill="#2a2ae8"/>
      <g>
        <rect x="0" y="207" width="130" height="6" fill="#e12a2a"/>
        <rect x="130" y="207" width="95" height="6" fill="#2a2ae8"/>
        <rect x="225" y="207" width="70" height="6" fill="#e12a2a"/>
        <rect x="295" y="207" width="105" height="6" fill="#2a2ae8"/>
      </g>
      <g font-family="Arial" font-size="7.5" font-weight="700" fill="#111">
        <text x="40" y="228">N</text><text x="88" y="228">D</text><text x="133" y="228">13</text><text x="188" y="228">F</text><text x="238" y="228">M</text><text x="286" y="228">A</text><text x="333" y="228">M</text><text x="382" y="228">J</text>
      </g>
    </symbol>
  </svg>

  <article class="abs post" style="top:148px">
    <h3 class="post-title">Westbrook Petroleum-Daily Report</h3>
    <span class="comments">0</span>
    <div class="meta">Friday, March 15, 2013 by Admin, Leave a comment</div>
    <svg class="chart" width="433" height="242" role="img" aria-label="Daily price chart for Westbrook Petroleum"><use href="#price-chart"/></svg>
    <p class="excerpt">Lorem ipsum dolor sit amet, consectetur adipiscing elit. Pellentesque et tortor vel metus malesuada iaculis. Vestibulum quis tincidunt velit, a eleifend nibh. Morbi nec nisi tristique odio semper hendrerit in a urna. Donec tempus leo in dictum molestie. Aliquam erat volutpat. Cras egestas egestas eros, in luctus quam dignissim sed. Donec faucibus ut lacus a faucibus. Donec posuere, nunc id vestibulum lacinia, nulla erat tincidunt sem, at pulvinar metus orci at tortor. Nulla nec venenatis urna, sit amet viverra sapien. Morbi id porttitor nisl. Pellentesque consectetur ipsum a nunc dictum aliquam. Curabitur dapibus ipsum sed orci semper eleifend. Suspendisse molestie ipsum lectus, a fermentum massa ultrices at.</p>
    <a class="more" href="#">LEARN MORE&gt;&gt;</a>
    <div class="ad-slot">AD HERE</div>
  </article>

  <div class="abs divider" style="top:630px"></div>

  <article class="abs post" style="top:641px">
    <h3 class="post-title">Westbrook Petroleum-Daily Report</h3>
    <span class="comments">0</span>
    <div class="meta">Friday, March 15, 2013 by Admin, Leave a comment</div>
    <svg class="chart" width="433" height="242" role="img" aria-label="Daily price chart for Westbrook Petroleum"><use href="#price-chart"/></svg>
    <p class="excerpt">Lorem ipsum dolor sit amet, consectetur adipiscing elit. Pellentesque et tortor vel metus malesuada iaculis. Vestibulum quis tincidunt velit, a eleifend nibh. Morbi nec nisi tristique odio semper hendrerit in a urna. Donec tempus leo in dictum molestie. Aliquam erat volutpat. Cras egestas egestas eros, in luctus quam dignissim sed. Donec faucibus ut lacus a faucibus. Donec posuere, nunc id vestibulum lacinia, nulla erat tincidunt sem, at pulvinar metus orci at tortor. Nulla nec venenatis urna, sit amet viverra sapien. Morbi id porttitor nisl. Pellentesque consectetur ipsum a nunc dictum aliquam. Curabitur dapibus ipsum sed orci semper eleifend. Suspendisse molestie ipsum lectus, a fermentum massa ultrices at.</p>
    <a class="more" href="#">LEARN MORE&gt;&gt;</a>
    <div class="ad-slot">AD HERE</div>
  </article>

  <aside>
    <h3 class="abs side side-title" style="top:110px">Newsletter</h3>
    <div class="abs side news-box">
      <div class="ribbon">Sign up</div>
      <div class="wanna">Wanna get<b>INSIDER NEWS?</b></div>
      <div class="news-note">Sign up to receive email updates.</div>
      <div class="field" style="top:77px">Your Name</div>
      <div class="field" style="top:97px">Your Email Address</div>
      <div class="submit">SUBMIT</div>
      <div class="privacy">*We Respect your Privacy</div>
    </div>

    <div class="abs side profile">
      <div class="photo" role="img" aria-label="Portrait photo of the blog author"></div>
      <p class="bio">Hello!<br>my name is <b>Marcus Pellingham</b><br>Lorem ipsum dolor sit amet, consectetur adipiscing elit. Pellentesque et tortor vel metus malesuada iaculis. Vestibulum quis tincidunt velit, a eleifend nibh. Morbi nec nisi tristique odio semper hendrerit in a urna. Donec tempus leo in dictum molestie. Aliquam erat volutpat.</p>
    </div>

    <h3 class="abs side side-title" style="top:553px">Recent blog post</h3>
    <ul class="abs side post-list" style="top:578px">
      <li>This is Dummy post place your text here..</li>
      <li>Sample Post here this is dummy text place your text here.</li>
      <li>This is Dummy post place your text here..</li>
      <li>Sample Post here this is dummy text place your text here.</li>
      <li>This is Dummy post place your text here..</li>
      <li>Sample Post here this is dummy text place your text here.</li>
    </ul>

    <h3 class="abs side side-title" style="top:759px">Archives</h3>
    <div class="abs side archive"><div class="select">Please Select</div></div>

    <div class="abs side promos">
      <h4>Torvex Promos</h4>
      <div class="promo"><a href="#">Send <b>Flowers</b> from $19.99</a>Send Roses, Lilies &amp; other <b>Flowers</b> "Best Value" - Daily Market Ledger<br><i>www.bloomcrate.com</i></div>
      <div class="promo"><a href="#"><b>Flowers</b> Delivered in AM</a>Have Your Order Hand Delivered First Thing in the Morning !<br><i>www.ShoreToShore<b>Blooms</b>.com</i></div>
      <div class="promo"><a href="#"><b>Flowers</b></a>Same Day Hand Delivery Guaranteed. Save $10 Online using Coupon JF<br><i>PetalHub.com/<b>Flowers</b>_Special</i></div>
      <div class="promo"><a href="#">Same Day <b>Flowers</b> For Less</a>Beautiful Fresh <b>Flowers</b> Under $30 Why Pay More? Quality <b>Flowers</b><br><i>www.StemsForYou.com</i></div>
      <div class="promo"><a href="#">Keepsake <b>Flowers</b></a>Holiday Flower Sale - Up To 10% Off Orders of $50 or More.<br><i>www.Keepsake<b>Blooms</b>.com</i></div>
    </div>
  </aside>

  <footer>
    <div class="abs footer">Home<span>|</span>About<span>|</span>Blog<span>|</span>Contacts<span>|</span>Disclaimer</div>
    <div class="abs base">Copyright 2013 pellinghamblog.com All Rights Reserved</div>
  </footer>

</div>
</div>
</body>
</html>
```